Professional, elegant brochure for funeral home

We have a funeral home. We would like a 2 sided brochure. On one side will be 3 columns for our cremation options and on the other side would be 2-3 columns of our burial options. Would like to print it and also will be putting it on our website at www.Veltranoserves.com

Use as examples

https://www.bardwellhaven.com/pricing-and-resources/online-cremation-package-options

https://pellingtonmortuary.com/wp-content/uploads/Cremation-with-Ceremony-Plans.pdf

We only need a simple 1page (front and back brochure). Once we have decided on the designer I can provide the final content to be placed on the brochure.

Target Market(s)

We are family owned business so Something soft, inviting, personable and looks professionally done.

Industry/Entity Type

Funeral Home

Requirements
Must have
• Look professional. Easy to read
Nice to have
• Softer Muted comforting colors. No bright colors.

```html
<!DOCTYPE html>
<html lang="en">
<head>
<meta charset="utf-8">
<title>Veltrano Funeral Home – Cremation and Burial Options</title>
<link rel="stylesheet" href="https://fonts.googleapis.com/css2?family=Archivo+Black&family=Libre+Baskerville:wght@400;700&family=Montserrat:wght@400;500&display=swap">
<style>
  :root{
    --canvas:#5a5a5a;
    --paper:#ffffff;
    --blue:#0b8ad6;
    --blue-deep:#0a7cc4;
    --green:#b6cf3c;
    --green-light:#c6da55;
    --header-grey:#ececec;
    --maroon:#6a1616;
    --overlay-blue:rgba(24,78,222,.86);
    --ink:#1d1d1d;
  }
  *{box-sizing:border-box;margin:0;padding:0}
  html,body{width:1200px;height:833px;overflow:hidden}
  body{background:var(--canvas);position:relative;font-family:"Montserrat",sans-serif}

  .sheet{position:absolute;top:75px;width:529px;height:683px;background:var(--paper)}
  .sheet--cremation{left:53px}
  .sheet--burial{left:619px}
  .sheet__inner{position:absolute;left:16px;top:17px;width:497px}

  .hero{position:relative;height:257px;overflow:hidden}
  .hero__photo{position:absolute;inset:0}
  .sheet--cremation .hero__photo{background:radial-gradient(ellipse at 30% 60%,#b8a58e 0%,#8d8a6c 35%,#5f6a4a 70%,#4a5238 100%)}
  .sheet--burial .hero__photo{background:linear-gradient(180deg,#2f3d2b 0%,#46563a 40%,#6f7a63 62%,#8d8676 82%,#5f5a4f 100%)}
  .hero__big{position:absolute;font-family:"Archivo Black",sans-serif;color:var(--overlay-blue);font-size:104px;line-height:.72;letter-spacing:-2px;white-space:nowrap}
  .hero__small{position:absolute;z-index:2;font-family:"Libre Baskerville",serif;font-weight:700;font-size:18px;line-height:1;color:#fff;letter-spacing:6px;white-space:nowrap}
  .sheet--cremation .hero__big{left:38px;top:160px}
  .sheet--cremation .hero__small{left:137px;top:188px}
  .sheet--burial .hero__big{left:43px;top:103px}
  .sheet--burial .hero__small{left:75px;top:136px}

  .brand{position:absolute;left:282px;top:60px;width:176px;text-align:center;color:#fff}
  .brand__name{font-family:"Libre Baskerville",serif;font-weight:400;font-size:17px;line-height:1.15}
  .brand__rule{height:1px;background:rgba(255,255,255,.8);margin:6px 0 4px}
  .brand__tag{font-family:"Libre Baskerville",serif;font-size:9.5px;white-space:nowrap}

  .band{height:38px;margin-top:7px;display:flex;align-items:center;justify-content:center;font-family:"Libre Baskerville",serif;font-weight:700;font-size:22px;letter-spacing:5px;color:#fff}
  .sheet--cremation .band{background:var(--blue)}
  .sheet--burial .band{background:var(--green)}

  .plans{display:grid;grid-template-columns:repeat(3,1fr)}
  .plan__title{height:49px;background:var(--header-grey);display:flex;align-items:center;justify-content:center;text-align:center;font-family:"Libre Baskerville",serif;font-weight:700;font-size:13px;line-height:1.25;color:var(--maroon)}
  .plan:nth-child(2) .plan__title{background:#f3f3f3}
  .plan__list{height:173px;list-style:none;padding:21px 8px 0 26px}
  .plan__list li{position:relative;font-size:9px;line-height:12px;margin-bottom:4.5px}
  .plan__list li::before{content:"✓";position:absolute;left:-11px;top:0;font-size:9px}
  .plan__price{height:36px;display:flex;align-items:center;justify-content:center;font-family:"Libre Baskerville",serif;font-weight:700;font-size:20px;color:#fff}
  .plan__foot{height:45px;position:relative;display:flex;align-items:center;justify-content:center;overflow:hidden}
  .plan__badge{font-family:"Libre Baskerville",serif;font-weight:700;font-size:10px;line-height:1.2;text-align:center;color:#fff}

  .sheet--cremation .plan__list{background:linear-gradient(90deg,var(--green),var(--green-light));color:var(--ink)}
  .sheet--cremation .plan__list li::before{color:var(--maroon)}
  .sheet--cremation .plan__price{background:var(--blue-deep)}
  .sheet--cremation .plan__foot{background:linear-gradient(90deg,var(--green),var(--green-light))}
  .sheet--burial .plan__list{background:linear-gradient(90deg,var(--blue-deep),var(--blue));color:#fff}
  .sheet--burial .plan__price{background:linear-gradient(90deg,var(--green),var(--green-light))}
  .sheet--burial .plan__foot{background:linear-gradient(90deg,var(--blue-deep),var(--blue))}
  .plan + .plan .plan__list,.plan + .plan .plan__price,.plan + .plan .plan__foot{border-left:1px solid rgba(255,255,255,.25)}

  .bouquet{position:absolute;left:12px;top:3px;width:60px;height:40px;border-radius:40% 40% 30% 30%;background:linear-gradient(180deg,#c04a86 0%,#c988a6 45%,#7fa548 100%);opacity:.85}
  .blossom{position:absolute;left:12px;top:9px;width:140px;height:28px;border-radius:14px;background:linear-gradient(90deg,#f3f6ea,#dfe9c9,#f5f7ef);opacity:.85}

  .contact{height:39px;margin-top:7px;display:flex;align-items:center;gap:12px;padding-left:53px;font-size:12px;color:#fff}
  .sheet--cremation .contact{background:var(--blue)}
  .sheet--burial .contact{background:var(--green)}
  .contact__item{display:flex;align-items:center;gap:4px;white-space:nowrap}
  .contact__item svg{width:11px;height:11px}
  .contact__social{width:14px;height:14px;border-radius:50%;background:#fff}
</style>
</head>
<body>

<section class="sheet sheet--cremation">
  <div class="sheet__inner">
    <header class="hero">
      <div class="hero__photo" role="img" aria-label="Photo of an elderly couple embracing outdoors"></div>
      <div class="brand">
        <div class="brand__name">Marco T. Veltrano<br>Funeral Home</div>
        <div class="brand__rule"></div>
        <div class="brand__tag">Cremation · Burial · Pre-Planning</div>
      </div>
      <div class="hero__big">AHEAD</div>
      <div class="hero__small">LIVE WELL, PLAN</div>
    </header>
    <h2 class="band">CREMATION OPTIONS</h2>
    <div class="plans">
      <article class="plan">
        <h3 class="plan__title">BASIC<br>CREMATION</h3>
        <ul class="plan__list">
          <li>Lorem ipsum dolor sit amet, consectetur</li><li>Lorem ipsum dolor sit amet, consectetur</li><li>Lorem ipsum dolor sit amet, consectetur</li><li>Lorem ipsum dolor sit amet, consectetur</li><li>Lorem ipsum dolor sit amet, consectetur</li>
        </ul>
        <div class="plan__price">$ 1.099.00</div>
        <div class="plan__foot"><div class="bouquet" role="img" aria-label="Bouquet of pink tulips"></div></div>
      </article>
      <article class="plan">
        <h3 class="plan__title">CREMATION<br>WITH CONFIDENCE</h3>
        <ul class="plan__list">
          <li>Lorem ipsum dolor sit amet, consectetur</li><li>Lorem ipsum dolor sit amet, consectetur</li><li>Lorem ipsum dolor sit amet, consectetur</li><li>Lorem ipsum dolor sit amet, consectetur</li><li>Lorem ipsum dolor sit amet, consectetur</li>
        </ul>
        <div class="plan__price">$ 1.799.00</div>
        <div class="plan__foot"><div class="plan__badge">MOST<br>POPULAR</div></div>
      </article>
      <article class="plan">
        <h3 class="plan__title">PREMIER<br>CREMATION</h3>
        <ul class="plan__list">
          <li>Lorem ipsum dolor sit amet, consectetur</li><li>Lorem ipsum dolor sit amet, consectetur</li><li>Lorem ipsum dolor sit amet, consectetur</li><li>Lorem ipsum dolor sit amet, consectetur</li><li>Lorem ipsum dolor sit amet, consectetur</li>
        </ul>
        <div class="plan__price">$ 2.499.00</div>
        <div class="plan__foot"><div class="blossom" role="img" aria-label="Branch of white blossoms"></div></div>
      </article>
    </div>
    <footer class="contact">
      <span class="contact__item"><svg viewBox="0 0 12 12" fill="none" stroke="#fff" stroke-width="1"><circle cx="6" cy="6" r="5"/><ellipse cx="6" cy="6" rx="2.2" ry="5"/><path d="M1 6h10"/></svg>www.veltranofh.com</span>
      <span class="contact__item"><svg viewBox="0 0 12 12" fill="none" stroke="#fff" stroke-width="1"><circle cx="6" cy="6" r="5"/><path d="M4 3.5l1 1.5-.6.8c.5 1 1.1 1.6 2 2l.7-.6 1.5 1-.6 1c-2.2-.3-4-2.2-4.3-4.4z" fill="#fff"/></svg>(555) 214-7730</span>
      <span class="contact__item"><svg viewBox="0 0 12 12" fill="none" stroke="#fff" stroke-width="1"><circle cx="6" cy="6" r="5"/><path d="M4 3.5l1 1.5-.6.8c.5 1 1.1 1.6 2 2l.7-.6 1.5 1-.6 1c-2.2-.3-4-2.2-4.3-4.4z" fill="#fff"/></svg>(555) 368-4152</span>
      <span class="contact__sep">|</span>
      <span class="contact__social"></span>
    </footer>
  </div>
</section>

<section class="sheet sheet--burial">
  <div class="sheet__inner">
    <header class="hero">
      <div class="hero__photo" role="img" aria-label="Photo of three generations fishing together on a wooden dock by a lake"></div>
      <div class="hero__big">LIFE</div>
      <div class="hero__small">CELEBRATE</div>
    </header>
    <h2 class="band">BURIAL OPTIONS</h2>
    <div class="plans">
      <article class="plan">
        <h3 class="plan__title">BASIC<br>BURIAL</h3>
        <ul class="plan__list">
          <li>Lorem ipsum dolor sit amet, consectetur</li><li>Lorem ipsum dolor sit amet, consectetur</li><li>Lorem ipsum dolor sit amet, consectetur</li><li>Lorem ipsum dolor sit amet, consectetur</li><li>Lorem ipsum dolor sit amet, consectetur</li>
        </ul>
        <div class="plan__price">$ 1.099.00</div>
        <div class="plan__foot"><div class="bouquet" role="img" aria-label="Bouquet of pink tulips"></div></div>
      </article>
      <article class="plan">
        <h3 class="plan__title">BURIAL WITH<br>CONFIDENCE</h3>
        <ul class="plan__list">
          <li>Lorem ipsum dolor sit amet, consectetur</li><li>Lorem ipsum dolor sit amet, consectetur</li><li>Lorem ipsum dolor sit amet, consectetur</li><li>Lorem ipsum dolor sit amet, consectetur</li><li>Lorem ipsum dolor sit amet, consectetur</li>
        </ul>
        <div class="plan__price">$ 1.799.00</div>
        <div class="plan__foot"><div class="plan__badge">MOST<br>POPULAR</div></div>
      </article>
      <article class="plan">
        <h3 class="plan__title">PREMIER<br>BURIAL</h3>
        <ul class="plan__list">
          <li>Lorem ipsum dolor sit amet, consectetur</li><li>Lorem ipsum dolor sit amet, consectetur</li><li>Lorem ipsum dolor sit amet, consectetur</li><li>Lorem ipsum dolor sit amet, consectetur</li><li>Lorem ipsum dolor sit amet, consectetur</li>
        </ul>
        <div class="plan__price">$ 2.499.00</div>
        <div class="plan__foot"><div class="blossom" role="img" aria-label="Branch of white blossoms"></div></div>
      </article>
    </div>
    <footer class="contact">
      <span class="contact__item"><svg viewBox="0 0 12 12" fill="none" stroke="#fff" stroke-width="1"><circle cx="6" cy="6" r="5"/><ellipse cx="6" cy="6" rx="2.2" ry="5"/><path d="M1 6h10"/></svg>www.veltranofh.com</span>
      <span class="contact__item"><svg viewBox="0 0 12 12" fill="none" stroke="#fff" stroke-width="1"><circle cx="6" cy="6" r="5"/><path d="M4 3.5l1 1.5-.6.8c.5 1 1.1 1.6 2 2l.7-.6 1.5 1-.6 1c-2.2-.3-4-2.2-4.3-4.4z" fill="#fff"/></svg>(555) 214-7730</span>
      <span class="contact__item"><svg viewBox="0 0 12 12" fill="none" stroke="#fff" stroke-width="1"><circle cx="6" cy="6" r="5"/><path d="M4 3.5l1 1.5-.6.8c.5 1 1.1 1.6 2 2l.7-.6 1.5 1-.6 1c-2.2-.3-4-2.2-4.3-4.4z" fill="#fff"/></svg>(555) 368-4152</span>
      <span class="contact__sep">|</span>
      <span class="contact__social"></span>
    </footer>
  </div>
</section>

</body>
</html>
```